Business Card Design Project

We need a logo design for a new company based in Southern California called "Brocklin Security Services, Inc." We install security and camera systems for homeowners and business, to protect their assets.
Updates

Project Deadline Extended
Reason: LOGO Design completes in eight days. Would like that design decided before we finish the business cards. Thanks...

Target Market(s)

Homeowners and business owners looking for additional protection of their assets.

Industry/Entity Type

Security

Font styles to use
Serif

Requirements
Must have
• Company Name
Office# 555-204-6137
Service# 555-204-6138
email: BrocklinSecurity@quorvex.net
address: 48210 Maple Row Larkmont Vale, NV 90000
Nice to have
• Serving Southern California

```html
<!DOCTYPE html>
<html lang="en">
<head>
<meta charset="utf-8">
<title>Brocklin Security Services, Inc. – Business Card</title>
<link rel="stylesheet" href="https://fonts.googleapis.com/css2?family=EB+Garamond:wght@400;500&display=swap">
<style>
  :root {
    --backdrop: #e6dfd5;
    --card-deep: #0a0932;
    --card-navy: #1e1f86;
    --card-royal: #2c46b4;
    --card-sky: #0a93dc;
    --accent-red: #dc2a2f;
    --text-light: #ffffff;
    --mark-grey: #c9cbd3;
  }
  * { margin: 0; padding: 0; box-sizing: border-box; }
  html, body {
    width: 1200px;
    height: 926px;
    overflow: hidden;
    background: var(--backdrop);
  }
  .canvas {
    position: relative;
    width: 1200px;
    height: 926px;
  }
  .business-card {
    position: absolute;
    left: 100px;
    top: 177px;
    width: 1000px;
    height: 572px;
    border-radius: 6px;
    overflow: hidden;
    background:
      radial-gradient(ellipse 70% 80% at 100% 100%, var(--card-sky) 0%, rgba(10,147,220,0) 70%),
      linear-gradient(135deg, var(--card-deep) 0%, var(--card-navy) 35%, var(--card-royal) 65%, var(--card-sky) 100%);
    box-shadow: 0 18px 40px rgba(0,0,0,0.25);
    font-family: "EB Garamond", Georgia, serif;
  }
  .brand-mark {
    position: absolute;
    left: 70px;
    top: 236px;
    display: flex;
    align-items: center;
    gap: 20px;
  }
  .brand-dot {
    width: 70px;
    height: 70px;
    border-radius: 50%;
    background: var(--accent-red);
  }
  .brand-name {
    color: var(--mark-grey);
    font-size: 64px;
    font-weight: 500;
    line-height: 1;
  }
  .contact-block {
    position: absolute;
    right: 50px;
    top: 52px;
    width: 520px;
    text-align: center;
    color: var(--text-light);
  }
  .company-name {
    color: var(--accent-red);
    font-size: 50px;
    font-weight: 500;
    line-height: 1.08;
    margin-bottom: 22px;
  }
  .contact-line {
    font-size: 34px;
    line-height: 1.22;
  }
  .contact-group { margin-bottom: 22px; }
  .tagline {
    color: var(--accent-red);
    font-size: 34px;
    line-height: 1.22;
  }
</style>
</head>
<body>
  <main class="canvas">
    <section class="business-card" aria-label="Brocklin Security Services business card">
      <div class="brand-mark">
        <span class="brand-dot" aria-hidden="true"></span>
        <span class="brand-name">Brocklin</span>
      </div>
      <div class="contact-block">
        <h1 class="company-name">Brocklin<br>Security Services Inc.</h1>
        <div class="contact-group">
          <p class="contact-line">Office (555)-204-6137</p>
          <p class="contact-line">Service (555)-204-6138</p>
        </div>
        <div class="contact-group">
          <p class="contact-line">48210 Maple Row</p>
          <p class="contact-line">Larkmont Vale, NV 90000</p>
        </div>
        <p class="contact-line">BrocklinSecurity@quorvex.net</p>
        <p class="tagline">Serving Southern California</p>
      </div>
    </section>
  </main>
</body>
</html>
```